Drowning Victims Recovery Website Design

We are working with Bluewake Recovery Dive Team. They provide recovery services for drowning victims so they can be reunited with their loved ones.

Some sites to use for inspiration:

https://cornerstoneplovik.org
https://www.steadfastmend.org
https://www.givingwellspring.org
https://www.pulsaid.ca/en

Thank you for taking the time to consider designing a website for us. We are web developers based in Stockton, CA, USA. Most of our projects go through the same process. Understanding this process may help you win a project with us. We custom-code all of our websites in-house. We don’t have any requirements as to what tools you use for your design, but we prefer Figma files. For any design that we label as four-stars, we send it to the client for review. The client picks the final design they want us to use. Once we complete this process, we will continue to show additional clients all the four-star sites and purchase them later. Your designs will have multiple chances to sell. For better chances of success, we ask that you follow these guidelines.

IMAGES:
If you use any images or icons in the design, we ask that you have a link to the asset so we can purchase the image/icon. Most of the designs we submit do not have the customer’s images on them unless they have some great images. Be creative; show us the feeling you are trying to portray with your image choices. Use any royalty-free site you choose. We subscribe to Varnex and mainly use their images, but we can purchase images outside of Varnex.

PLEASE NOTE: we will not submit designs to clients with watermarks on the images.

FONTS:
We ask that you identify the fonts used in the design. This can be done in a message if you want. We typically use Google Fonts and Varnex Fonts.

CONTENT:
We're always open to different content and ideas. We often submit designs with stock images so the client can see our vision. We typically take pictures after the website launch to use their images with our vision. Lorem Ipsum is fine for paragraphs, but we ask that you write the headers in correct English. We want to be able to show the vision and identify the sections of the website.

INSPIRATION:
We typically add a couple of links in the brief of websites we like to help you get started in your design.

REVISIONS:
We do not often ask for revisions of the designs unless we see something in the design that may not appeal to the client. If there are slight changes that we want to make, we do that in the development process.

FEEDBACK:
We rarely give feedback on designs during the design process. We are working on many website projects and do not have the time to provide feedback. We usually respond if your request is well thought out and asks specific questions, but a note asking “feedback, please” usually goes unanswered.

```html
<!DOCTYPE html>
<html lang="en">
<head>
<meta charset="utf-8">
<title>Bluewake Recovery Dive Team</title>
<link href="https://fonts.googleapis.com/css2?family=Roboto+Condensed:wght@400;700&family=Roboto:wght@400;500&display=swap" rel="stylesheet">
<style>
:root{
  --blue:#2b5677;
  --blue-dark:#1e4563;
  --navy:#0b1f35;
  --red:#b5090d;
  --red-bright:#d0141a;
  --white:#ffffff;
  --text:#4a4a4a;
  --mist:#eef2f5;
}
*{margin:0;padding:0;box-sizing:border-box}
html,body{width:1200px;height:4515px;overflow:hidden}
body{position:relative;background:var(--white);font-family:"Roboto",Arial,sans-serif;color:var(--text)}
.abs{position:absolute}
.cond{font-family:"Roboto Condensed","Arial Narrow",sans-serif}
.btn{position:absolute;display:flex;align-items:center;justify-content:center;font-family:"Roboto Condensed",sans-serif;font-weight:700;font-size:19px;color:var(--white);text-transform:uppercase;clip-path:polygon(0 0,94% 0,100% 20%,100% 100%,6% 100%,0 80%)}
.btn-red{background:var(--red)}
.btn-blue{background:var(--blue)}

/* header */
.site-header{position:absolute;left:0;top:0;width:1200px;height:140px;background:var(--white);border-top:5px solid var(--blue)}
.brand{position:absolute;left:126px;top:40px;font-family:"Roboto Condensed",sans-serif;font-weight:700;font-size:24px;line-height:26px;color:var(--blue);text-transform:uppercase}
.topbar{position:absolute;left:659px;top:0;width:541px;height:56px;background:var(--blue)}
.topbar .donate{position:absolute;left:0;top:0;width:215px;height:56px;background:var(--red);clip-path:polygon(0 0,100% 0,88% 100%,4% 100%);display:flex;align-items:center;justify-content:center;gap:8px;color:#fff;font:700 17px "Roboto Condensed",sans-serif}
.topbar .call{position:absolute;left:232px;top:0;height:56px;display:flex;align-items:center;gap:10px;color:#fff;font:700 17px "Roboto Condensed",sans-serif}
.main-nav{position:absolute;top:97px;left:0;width:1200px;font:700 16px "Roboto Condensed",sans-serif;color:var(--blue)}
.main-nav a{position:absolute;transform:translateX(-50%);text-decoration:none;color:inherit}
.main-nav a.active{color:var(--red)}

/* hero */
.hero-art{position:absolute;left:0;top:140px}
.hero-title{position:absolute;left:126px;top:282px;font:700 58px/60px "Roboto Condensed",sans-serif;color:#fff;text-transform:uppercase}
.hero-sub{position:absolute;left:128px;top:410px;font:700 31px "Roboto Condensed",sans-serif;color:#fff}

/* about */
.about-title{position:absolute;left:569px;top:918px;font:700 47px/58px "Roboto Condensed",sans-serif;color:#fff;text-transform:uppercase}
.about-text{position:absolute;left:569px;top:1048px;width:440px;font-size:15.5px;line-height:25px;color:#e6eef4}

/* stages */
.section-title{position:absolute;left:0;width:1200px;text-align:center;font:700 47px/58px "Roboto Condensed",sans-serif;color:var(--blue);text-transform:uppercase}
.section-title em{font-style:normal;color:var(--red)}
.stage{position:absolute;width:210px;text-align:center}
.stage h3{font:700 16px "Roboto Condensed",sans-serif;color:#222;text-transform:uppercase;margin-bottom:10px}
.stage p{font-size:13.5px;line-height:17px;color:#666}

/* rescue */
.rescue{position:absolute;left:0;top:2102px;width:1200px;height:678px;background:var(--red)}
.rescue-text{position:absolute;left:218px;top:2256px;width:764px;text-align:center;font-size:15.5px;line-height:25px;color:#fff}
.video-frame{position:absolute;left:133px;top:2491px;width:932px;height:493px;background:#fff;border-radius:26px;box-shadow:0 18px 40px rgba(0,0,0,.18)}
.video-media{position:absolute;left:16px;top:16px;width:900px;height:463px;border-radius:18px;background:linear-gradient(180deg,#3a2f3c 0%,#b05a2c 35%,#e28a36 48%,#7a3a1e 62%,#3d2418 100%)}

/* news */
.news-bg{position:absolute;left:0;top:3600px;width:1200px;height:500px;background:linear-gradient(180deg,#fff 0%,var(--mist) 40%,#dfe6ec 100%)}
.card{position:absolute;top:3217px;width:291px;height:483px;background:#fff;box-shadow:0 6px 22px rgba(0,0,0,.08)}
.card .media{height:220px}
.card h3{margin:26px 34px 0;font:700 18.5px/23px "Roboto Condensed",sans-serif;color:var(--blue);text-transform:uppercase}
.card p{margin:18px 34px 0;font-size:15px;line-height:23px;color:#555}
.card .more{position:absolute;left:34px;top:438px;font:700 15.5px "Roboto Condensed",sans-serif;color:var(--red)}

/* footer */
.footer-art{position:absolute;left:0;top:3930px}
.footer-brand{position:absolute;left:126px;top:4190px;font:700 38px/44px "Roboto Condensed",sans-serif;color:#fff;text-transform:uppercase}
.vline{position:absolute;width:1px;background:rgba(255,255,255,.3)}
.footer-head{position:absolute;font:700 22px "Roboto Condensed",sans-serif;color:#fff;text-transform:uppercase}
.footer-links{position:absolute;left:610px;top:4193px;list-style:none;font-size:15.5px;line-height:30.5px;color:#fff}
.contact-item{position:absolute;left:864px;display:flex;align-items:center;gap:16px;color:#fff;font-size:15.5px;line-height:21px}
.contact-item .dot{width:38px;height:38px;border-radius:50%;background:var(--red);display:flex;align-items:center;justify-content:center;flex:none}
.social{position:absolute;top:4412px;width:40px;height:40px;border-radius:50%;border:2px solid rgba(255,255,255,.5)}
.social.first{background:var(--red);border-color:var(--red)}
.hline{position:absolute;left:280px;top:4432px;width:792px;height:1px;background:rgba(255,255,255,.3)}
.copyright{position:absolute;left:0;top:4462px;width:1200px;text-align:center;font-size:13px;color:#dfe8ef}
</style>
</head>
<body>

<!-- hero and about backdrop -->
<svg class="hero-art" width="1200" height="1258" viewBox="0 0 1200 1258" aria-hidden="false">
  <defs>
    <linearGradient id="heroSea" x1="0" y1="0" x2="1" y2="0.4">
      <stop offset="0" stop-color="#03111f"/>
      <stop offset="0.45" stop-color="#0b3f72"/>
      <stop offset="1" stop-color="#0d5fa3"/>
    </linearGradient>
    <linearGradient id="aboutSea" x1="0" y1="0" x2="0" y2="1">
      <stop offset="0" stop-color="#2a5575"/>
      <stop offset="1" stop-color="#2d5a7b"/>
    </linearGradient>
  </defs>
  <rect x="0" y="440" width="1200" height="818" fill="url(#aboutSea)" role="img" aria-label="Faint underwater photo of divers behind the about section"/>
  <polygon points="0,470 600,683 1200,470 1200,520 600,683 0,520" fill="var(--red)"/>
  <polygon points="0,0 1200,0 1200,480 600,650 0,480" fill="url(#heroSea)" role="img" aria-label="Scuba diver swimming through deep blue water with rising bubbles"/>
</svg>

<header class="site-header">
  <div class="brand">Bluewake Recovery<br>Dive Team</div>
  <div class="topbar">
    <div class="donate">
      <svg width="16" height="14" viewBox="0 0 16 14"><path d="M8 14 1.2 7.2A4 4 0 0 1 8 1.8a4 4 0 0 1 6.8 5.4Z" fill="#fff"/></svg>
      DONATE NOW
    </div>
    <div class="call">
      <svg width="16" height="16" viewBox="0 0 24 24"><path d="M6.6 10.8a15 15 0 0 0 6.6 6.6l2.2-2.2c.3-.3.7-.4 1-.2 1.1.4 2.3.6 3.6.6.6 0 1 .4 1 1V20c0 .6-.4 1-1 1A17 17 0 0 1 3 4c0-.6.4-1 1-1h3.5c.6 0 1 .4 1 1 0 1.3.2 2.5.6 3.6.1.3 0 .7-.2 1Z" fill="#fff"/></svg>
      CALL: 041 552 7180
    </div>
  </div>
  <nav class="main-nav">
    <a class="active" style="left:427px">HOME</a>
    <a style="left:527px">ABOUT</a>
    <a style="left:640px">SERVICES</a>
    <a style="left:748px">TEAM</a>
    <a style="left:885px">LATEST UPDATES</a>
    <a style="left:1039px">CONTACT</a>
  </nav>
</header>

<h1 class="hero-title">Bluewake Recovery<br>Dive Team</h1>
<p class="hero-sub">Drowning Victims Recovery</p>
<a class="btn btn-red" style="left:130px;top:466px;width:178px;height:54px">Contact Us</a>

<!-- about -->
<svg class="abs" style="left:161px;top:904px" width="326" height="364" viewBox="0 0 326 364">
  <defs>
    <linearGradient id="shieldSea" x1="0" y1="0" x2="1" y2="1">
      <stop offset="0" stop-color="#0e6da8"/>
      <stop offset="0.6" stop-color="#1b8dc2"/>
      <stop offset="1" stop-color="#0a4f7e"/>
    </linearGradient>
  </defs>
  <path d="M163 8C120 34 60 44 8 36V170C8 268 90 328 163 356C236 328 318 268 318 170V36C266 44 206 34 163 8Z" fill="url(#shieldSea)" stroke="#fff" stroke-width="10" role="img" aria-label="Diver with fins descending through clear blue water"/>
</svg>
<h2 class="about-title">About Bluewake<br>Recovery Dive Team</h2>
<p class="about-text">Lorem ipsum dolor sit amet, consectetur adipiscing elit, sed do eiusmod tempor incididunt ut labore et dolore magna aliq ua. Quis ipsum suspendisse ultrices gravida. Risus commodo viverra maecenas accumsan lacus vel facilisis.</p>
<a class="btn btn-red" style="left:573px;top:1186px;width:179px;height:54px">Read More</a>

<!-- stages -->
<h2 class="section-title" style="top:1494px">The <em>Four Stages</em> In<br>Drowning Victim Search</h2>
<svg class="abs" style="left:0;top:1655px" width="1200" height="194" viewBox="0 0 1200 194">
  <line x1="290" y1="76" x2="900" y2="76" stroke="var(--blue)" stroke-width="4"/>
  <g fill="#fff" stroke-width="8">
    <path d="M212 6C190 22 160 26 132 20V98C132 148 172 174 212 188C252 174 292 148 292 98V20C264 26 234 22 212 6Z" stroke="var(--red)" transform="translate(0,0)"/>
    <path d="M212 6C190 22 160 26 132 20V98C132 148 172 174 212 188C252 174 292 148 292 98V20C264 26 234 22 212 6Z" stroke="var(--blue)" transform="translate(256,0)"/>
    <path d="M212 6C190 22 160 26 132 20V98C132 148 172 174 212 188C252 174 292 148 292 98V20C264 26 234 22 212 6Z" stroke="var(--red)" transform="translate(512,0)"/>
    <path d="M212 6C190 22 160 26 132 20V98C132 148 172 174 212 188C252 174 292 148 292 98V20C264 26 234 22 212 6Z" stroke="var(--blue)" transform="translate(767,0)"/>
  </g>
  <!-- warning -->
  <g fill="none" stroke="var(--blue)" stroke-width="4" stroke-linejoin="round">
    <path d="M212 52 244 108H180Z"/>
    <line x1="212" y1="72" x2="212" y2="92"/>
    <circle cx="212" cy="100" r="1.5" fill="var(--blue)"/>
  </g>
  <!-- binoculars -->
  <g fill="none" stroke="var(--blue)" stroke-width="4">
    <rect x="442" y="54" width="16" height="22" rx="3"/>
    <rect x="478" y="54" width="16" height="22" rx="3"/>
    <circle cx="450" cy="96" r="13"/>
    <circle cx="486" cy="96" r="13"/>
    <line x1="462" y1="86" x2="474" y2="86"/>
  </g>
  <!-- ship -->
  <g fill="none" stroke="var(--blue)" stroke-width="4" stroke-linejoin="round">
    <path d="M694 96 702 112H746L754 96Z"/>
    <rect x="704" y="76" width="40" height="20"/>
    <rect x="716" y="58" width="16" height="18"/>
    <path d="M690 122q8-6 17 0t17 0 17 0 17 0"/>
  </g>
  <!-- waves -->
  <g fill="none" stroke="var(--blue)" stroke-width="4">
    <path d="M948 70q8-7 16 0t16 0 16 0 16 0"/>
    <path d="M948 84q8-7 16 0t16 0 16 0 16 0"/>
    <path d="M948 98q8-7 16 0t16 0 16 0 16 0"/>
  </g>
</svg>
<div class="stage" style="left:107px;top:1872px"><h3>First Response</h3><p>Lorem ipsum dolor sit amet consectetur adipiscing elit sedo eiusmod tempor incididunt.</p></div>
<div class="stage" style="left:363px;top:1872px"><h3>Watchfully Stand-By</h3><p>Lorem ipsum dolor sit amet consectetur adipiscing elit sedo eiusmod tempor incididunt.</p></div>
<div class="stage" style="left:619px;top:1872px"><h3>Active Search</h3><p>Lorem ipsum dolor sit amet consectetur adipiscing elit sedo eiusmod tempor incididunt.</p></div>
<div class="stage" style="left:874px;top:1872px"><h3>Disengaged Waiting</h3><p>Lorem ipsum dolor sit amet consectetur adipiscing elit sedo eiusmod tempor incididunt.</p></div>

<!-- rescue -->
<section class="rescue"></section>
<h2 class="section-title" style="top:2180px;color:#fff">Rescue &amp; Recovery</h2>
<p class="rescue-text">Lorem ipsum dolor sit amet, consectetur adipiscing elit, sed do eiusmod tempor incididunt ut labore et dolore magna aliqua. Quis ipsum suspendisse ultrices gravida. Risus commodo viverra maecenas accumsan lacus vel facilisisorem ipsum dolor sit amet, consectetur adipiscing elit, sed do eiusmod tempor incididunt ut labore et dolore magna aliq ua. Quis ipsum susp maecenas accumsl facilisis.</p>
<a class="btn btn-blue" style="left:510px;top:2388px;width:179px;height:53px">Read More</a>
<div class="video-frame">
  <div class="video-media" role="img" aria-label="Divers with air tanks wading into the sea at sunset"></div>
  <svg class="abs" style="left:416px;top:190px" width="100" height="100" viewBox="0 0 100 100">
    <circle cx="50" cy="50" r="45" fill="none" stroke="#fff" stroke-width="6"/>
    <path d="M40 30 70 50 40 70Z" fill="#fff"/>
  </svg>
</div>

<!-- news -->
<div class="news-bg" role="img" aria-label="Soft pale water surface"></div>
<h2 class="section-title" style="top:3101px"><em>Latest News</em> And Updates</h2>
<article class="card" style="left:126px">
  <div class="media" role="img" aria-label="Hand reaching from splashing water toward an orange life ring" style="background:linear-gradient(135deg,#4d6f80,#c96a38 55%,#3f5d6c)"></div>
  <h3>Lorem Ipsum Dolor Sit Amet Consectetur</h3>
  <p>Lorem ipsum dolor sit ametcons ectetur adipiscing elitsed lordo eiusmod tempor inci diduntuta borpor inci didue.</p>
  <span class="more">Read Full Story ›</span>
</article>
<article class="card" style="left:454px">
  <div class="media" role="img" aria-label="Divers silhouetted against light in deep blue water" style="background:radial-gradient(circle at 55% 30%,#3da2e8,#0b3c86 55%,#06183e)"></div>
  <h3>Lorem Ipsum Dolor Sit Amet Consectetur</h3>
  <p>Lorem ipsum dolor sit ametcons ectetur adipiscing elitsed lordo eiusmod tempor inci diduntuta borpor inci didue.</p>
  <span class="more">Read Full Story ›</span>
</article>
<article class="card" style="left:783px">
  <div class="media" role="img" aria-label="Divers with tanks entering the sea at sunset" style="background:linear-gradient(180deg,#3a2f3c,#d27a34 45%,#4a2a1a)"></div>
  <h3>Lorem Ipsum Dolor Sit Amet Consectetur</h3>
  <p>Lorem ipsum dolor sit ametcons ectetur adipiscing elitsed lordo eiusmod tempor inci diduntuta borpor inci didue.</p>
  <span class="more">Read Full Story ›</span>
</article>
<a class="btn btn-red" style="left:499px;top:3758px;width:204px;height:53px">View All News</a>

<!-- footer -->
<svg class="footer-art" width="1200" height="585" viewBox="0 0 1200 585">
  <polygon points="0,208 600,9 1200,208 1200,585 0,585" fill="var(--red)"/>
  <polygon points="0,212 600,38 1200,212 1200,585 0,585" fill="var(--blue)"/>
</svg>
<div class="footer-brand">Bluewake Recovery<br>Dive Team</div>
<div class="vline" style="left:526px;top:4147px;height:207px"></div>
<div class="vline" style="left:780px;top:4147px;height:207px"></div>
<div class="footer-head" style="left:608px;top:4146px">Links</div>
<ul class="footer-links">
  <li>Home</li><li>About</li><li>Services</li><li>Team</li><li>Latest Updates</li><li>Contact</li>
</ul>
<div class="footer-head" style="left:862px;top:4137px">Contact</div>
<div class="contact-item" style="top:4186px">
  <span class="dot"><svg width="14" height="18" viewBox="0 0 14 18"><path d="M7 18S0 10.5 0 7a7 7 0 0 1 14 0c0 3.5-7 11-7 11Z" fill="#fff"/><circle cx="7" cy="7" r="2.6" fill="var(--red)"/></svg></span>
  <span>Lorem Dummyloac<br>Lor 345 Pind 338</span>
</div>
<div class="contact-item" style="top:4246px">
  <span class="dot"><svg width="16" height="16" viewBox="0 0 24 24"><path d="M6.6 10.8a15 15 0 0 0 6.6 6.6l2.2-2.2c.3-.3.7-.4 1-.2 1.1.4 2.3.6 3.6.6.6 0 1 .4 1 1V20c0 .6-.4 1-1 1A17 17 0 0 1 3 4c0-.6.4-1 1-1h3.5c.6 0 1 .4 1 1 0 1.3.2 2.5.6 3.6.1.3 0 .7-.2 1Z" fill="#fff"/></svg></span>
  <span>Phone:<br>418 627 3305</span>
</div>
<div class="contact-item" style="top:4306px">
  <span class="dot"><svg width="16" height="12" viewBox="0 0 16 12"><rect width="16" height="12" rx="1.5" fill="#fff"/><path d="M1 1 8 7l7-6" fill="none" stroke="var(--red)" stroke-width="1.6"/></svg></span>
  <span>Email:<br>info@bluewakedive.org</span>
</div>
<span class="social first" style="left:134px"></span>
<span class="social" style="left:181px"></span>
<span class="social" style="left:231px"></span>
<div class="hline"></div>
<p class="copyright">Copyright © 2025 All rights are reserved.</p>

</body>
</html>
```